Driftwood Sailing. Explore the Whitsundays We Dare You

Hello,
I have a catamaran charter business in the Whitsunday Islands, Australia.
My business is called Driftwood Sailing and my catamaran is a Maristo 380 K4 and his name is Quiet Tern. I have attached its logo but would like something for Driftwood Sailing.
I am looking for a website for my business.
I'm also after 1 logos (for Driftwood Sailing).
I would like to be able to edit the website if needed (putting photos into the gallery, post reviews) and I'll need a shopping cart and all the usual social media contacts.
I will also need a live availability calendar for people to look at to see if the dates they want are available. I will need to easily edit this.
It must also stand out. I can supply most of the picture and maybe some video.
There will only be about 7 pages -
Home - Pictures scrolling past
Price and Availability - Have to show a live calendar that people can click on to see if the dates they want are available.
Gallery - I will put up photos and comments from past charterers.
Contact - A form they fill out to ask questions
Testimonials & Reviews - People can submit photos and review. I will have to be able to easily edit them.
Bookings & Store - If they want to pay by card, or if they want to buy any merchandise and so it would need a shopping cart.
Misc Page - What to bring, What to expect, etc etc
At the moment I only have 1 catamaran that will be advertised but I may get another at a later date.
The site will need a chilled out feel as people will be coming to the Whitsundays to relax and sail around.
The font needs to be a friendly font if this is possible.
The photo I uploaded called Anchor Tattoo is the logo I want for Driftwood Sailing.
Hope this helps.
Does this sound do-able

Target Market(s)

20 - 60

Industry/Entity Type

Tourism

Coding

Coded - Design and coding required

Number of Pages Required

5+ page

Colors

Designer to choose colors to be used in the design.

Requirements
Must have
• Chilled out feel

```html
<!DOCTYPE html>
<html lang="en">
<head>
<meta charset="utf-8">
<title>Quiet Tern — Driftwood Sailing</title>
<link href="https://fonts.googleapis.com/css2?family=Lato:wght@300;400;700;900&display=swap" rel="stylesheet">
<style>
:root{
  --orange:#e8693a;
  --orange-dark:#d9572a;
  --ink:#222;
  --text:#555;
  --muted:#9a9a9a;
  --line:#d8d8d8;
  --green:#1f6b1f;
  --red:#c8102e;
  --star:#f2c200;
  --white:#fff;
  --navy:#1f3b5a;
}
*{box-sizing:border-box;margin:0;padding:0}
html,body{width:1200px;height:4358px;overflow:hidden}
body{position:relative;font-family:'Lato',sans-serif;color:var(--text);background:var(--white)}
.abs{position:absolute}

/* header */
.site-header{left:0;top:0;width:1200px;height:116px;background:var(--white)}
.brand{display:flex;align-items:center;gap:12px;font-size:26px;font-weight:700;color:var(--navy);white-space:nowrap}
.brand-dot{width:26px;height:26px;border-radius:50%;background:var(--orange)}
.header-brand{left:100px;top:40px}
.main-nav{left:345px;top:48px;display:flex;gap:24px;font-size:14px;color:var(--ink);white-space:nowrap}
.main-nav .active{color:var(--orange)}
.cart{left:1064px;top:40px;width:34px;height:34px;border-radius:50%;background:var(--orange);display:flex;align-items:center;justify-content:center}

/* hero */
.hero{left:0;top:116px;width:1200px;height:581px;overflow:hidden}
.hero-photo{position:absolute;inset:0;background:radial-gradient(circle at 640px 90px,#ffe9a8 0,#f5b24a 60px,#b86a2a 180px,transparent 330px),linear-gradient(180deg,#3a2c22 0%,#6a4a2e 35%,#8a6a48 55%,#3f3a35 75%,#1f1c1a 100%)}
.hero-mark{left:848px;top:72px;width:64px;height:64px;border:4px solid var(--white);border-radius:50%}
.hero-title{left:660px;top:170px;width:440px;text-align:center;font-size:62px;font-weight:700;color:var(--white);white-space:nowrap}
.hero-sub{left:640px;top:266px;width:480px;text-align:center;font-size:17px;color:var(--white);white-space:nowrap}
.hero-btn{left:812px;top:328px;width:136px;height:44px;border:2px solid var(--white);border-radius:22px;color:var(--white);font-size:12px;font-weight:700;display:flex;align-items:center;justify-content:center;letter-spacing:.5px}
.hero-dots{left:538px;top:467px;display:flex;gap:10px}
.hero-dots span{width:12px;height:12px;border-radius:50%;border:2px solid var(--white)}
.hero-dots .on{background:var(--white)}
.hero-wave{left:0;top:520px}

/* price */
.section-mark{left:572px;top:712px;width:56px;height:56px;border-radius:50%;border:4px solid var(--orange)}
.calendar{left:100px;top:813px;width:250px;background:var(--white);box-shadow:0 4px 8px rgba(0,0,0,.25)}
.cal-head{height:36px;background:#2b2b2b;color:var(--white);display:flex;align-items:center;justify-content:space-between;padding:0 12px;font-size:16px;font-weight:700}
.cal-days,.cal-grid{display:grid;grid-template-columns:repeat(7,1fr);gap:3px;padding:3px 4px}
.cal-days span{font-size:9px;text-align:center;color:#777}
.cal-grid span{height:29px;font-size:11px;font-weight:700;color:var(--white);display:flex;align-items:center;justify-content:center}
.b{background:var(--red)} .a{background:var(--green)} .o{background:#e6e6e6;color:#999!important}
.legend{left:130px;top:1090px;display:flex;gap:40px;font-size:12px;color:var(--ink)}
.legend i{display:inline-block;width:12px;height:12px;border-radius:50%;margin-right:10px;vertical-align:-1px}
.price-title{left:421px;top:800px;font-size:50px;font-weight:400;color:var(--ink);white-space:nowrap}
.price-text{left:423px;top:872px;width:690px;font-size:14px;line-height:28px;color:var(--muted)}
.price-text p+p{margin-top:2px}
.btn{background:var(--orange);color:var(--white);font-size:12px;font-weight:700;border-radius:24px;display:flex;align-items:center;justify-content:center;gap:6px;white-space:nowrap}
.price-btn{left:424px;top:1063px;width:134px;height:44px}

/* gallery */
.gallery{left:0;top:1200px;width:1200px;height:456px;background:linear-gradient(180deg,#b9bfb9 0%,#d7dbd6 40%,#eef0ee 70%,#dde2da 100%)}
.gallery-title{left:0;top:80px;width:1200px;text-align:center;font-size:48px;color:var(--ink)}
.gal-tile{top:180px;width:243px;height:189px;border:3px solid var(--white)}
.gal-card{left:18px;top:18px;width:201px;height:147px;background:rgba(232,105,58,.9);color:var(--white);text-align:center;padding-top:50px}
.gal-card h3{font-size:17px;font-weight:400}
.gal-card p{font-size:12px;margin-top:12px}
.gal-arrow{top:240px}

/* contact */
.contact-title{left:0;top:1735px;width:1200px;text-align:center;font-size:48px;color:var(--ink)}
.field label{display:block;font-size:13px;color:var(--ink);margin-bottom:12px}
.field .box{width:334px;height:44px;border:1px solid var(--line)}
.field .box.wide{width:694px;height:102px}
.send-btn{left:813px;top:2202px;width:134px;height:41px;border-radius:22px;background:#1d1d1d;color:var(--white);font-size:12px;font-weight:700;display:flex;align-items:center;justify-content:center}

/* testimonials */
.testimonials{left:0;top:2339px;width:1200px;height:479px;background:var(--orange)}
.testi-title{left:0;top:60px;width:1200px;text-align:center;font-size:48px;color:var(--white);font-weight:700}
.review{top:177px;width:330px;display:flex;gap:22px}
.avatar{flex:none;width:72px;height:72px;border-radius:50%;border:3px solid var(--white)}
.review q{display:block;font-size:11px;font-style:italic;color:var(--white);line-height:18px;quotes:none}
.review .name{font-size:10px;font-weight:700;color:var(--white);margin-top:10px;letter-spacing:.5px}
.review .role{font-size:10px;color:#ffe0d0;margin-top:4px}
.stars{display:flex;gap:4px;margin-top:16px}
.t-arrow{top:230px;width:34px;height:34px;border-radius:50%;border:2px solid #f6b596;display:flex;align-items:center;justify-content:center}

/* bookings & store */
.h2{font-size:33px;color:var(--ink);font-weight:700}
.book-text{left:96px;top:2960px;width:420px;font-size:14px;line-height:25px;color:var(--muted)}
.book-photo{left:96px;top:3074px;width:372px;height:223px;background:linear-gradient(180deg,#8fa3b0 0%,#6b8394 30%,#2c3b6d 55%,#3a4a86 70%,#9aa4a8 100%)}
.book-btn{left:96px;top:3328px;width:134px;height:43px}
.divider{left:532px;top:2990px;width:1px;height:260px;background:var(--line)}
.product{top:2992px;width:236px;text-align:center}
.product .img{height:183px;background:#f1f1f1;border:1px solid #e4e4e4;display:flex;align-items:center;justify-content:center}
.product h4{font-size:17px;font-weight:400;color:var(--ink);margin-top:22px;white-space:nowrap}
.product .price{font-size:16px;color:var(--muted);margin-top:12px}
.product .shop{display:inline-block;margin-top:12px;border:1px solid var(--orange);color:var(--orange);font-size:11px;font-weight:700;border-radius:14px;padding:6px 16px}
.s-arrow{top:3337px;width:32px;height:32px;border-radius:50%;border:1px solid #999;display:flex;align-items:center;justify-content:center}

/* extras band */
.extras{left:0;top:3472px;width:1200px;height:406px;overflow:hidden}
.extras a{position:absolute;top:180px;font-size:38px;font-weight:900;color:var(--white);text-decoration:underline;text-underline-offset:6px;text-decoration-thickness:3px;white-space:nowrap}
.extras-mark{left:543px;top:145px;width:116px;height:116px;border-radius:50%;background:var(--orange);border:4px solid rgba(255,255,255,.5)}

/* footer */
.footer-brand{left:100px;top:3988px}
.socials{left:98px;top:4083px;display:flex;gap:10px}
.socials span{width:34px;height:34px;border-radius:50%}
.foot-h{font-size:22px;font-weight:700;color:var(--ink);white-space:nowrap}
.links{left:465px;top:4015px;list-style:none;font-size:13px;color:var(--ink);line-height:31px}
.vline{left:440px;top:3966px;width:1px;height:250px;background:var(--line)}
.news-text{left:726px;top:4005px;font-size:13px;color:var(--ink);white-space:nowrap}
.news-input{left:726px;top:4052px;width:355px;height:34px;border:1px solid var(--line);border-radius:18px;font-size:12px;color:var(--muted);padding:9px 16px}
.subscribe{left:726px;top:4102px;width:114px;height:35px}
.foot-line{left:96px;top:4276px;width:1008px;height:1px;background:var(--line)}
.copy{left:0;top:4306px;width:1200px;text-align:center;font-size:12px;color:var(--ink)}
</style>
</head>
<body>

<header class="site-header abs">
  <div class="brand header-brand abs"><span>Quiet Tern</span><span class="brand-dot"></span></div>
  <nav class="main-nav abs">
    <span class="active">Home</span><span>Price and Availability</span><span>Gallery</span><span>Contact</span><span>Testimonials &amp; Reviews</span><span>Bookings &amp; Store</span><span>Misc</span>
  </nav>
  <div class="cart abs">
    <svg width="18" height="16" viewBox="0 0 18 16"><path d="M1 1h3l2 9h9l2-7H5" fill="none" stroke="#fff" stroke-width="2"/><circle cx="7" cy="14" r="1.5" fill="#fff"/><circle cx="14" cy="14" r="1.5" fill="#fff"/></svg>
  </div>
</header>

<section class="hero abs">
  <div class="hero-photo" role="img" aria-label="Sunset over a calm Whitsunday bay with two people walking along the beach"></div>
  <div class="hero-mark abs"></div>
  <h1 class="hero-title abs">Quiet Tern</h1>
  <p class="hero-sub abs">Sed utperspiciomis iste natus error sit voluptatem</p>
  <div class="hero-btn abs">GET STARTED</div>
  <div class="hero-dots abs"><span class="on"></span><span></span><span></span><span></span><span></span><span></span></div>
  <svg class="hero-wave abs" width="1200" height="61" viewBox="0 0 1200 61" preserveAspectRatio="none">
    <path d="M0 0 C300 55 900 55 1200 0 L1200 61 L0 61Z" fill="#fff"/>
    <path d="M0 0 C300 40 900 40 1200 -5 L1200 10 C900 60 300 60 0 18Z" fill="#e8693a"/>
    <path d="M0 30 C300 66 900 66 1200 22 L1200 30 C900 70 300 70 0 40Z" fill="#e8693a"/>
  </svg>
</section>

<div class="section-mark abs"></div>

<section class="price">
  <div class="calendar abs">
    <div class="cal-head"><span>&#8249;</span><span>MAY 2018</span><span>&#8250;</span></div>
    <div class="cal-days"><span>MON</span><span>TUE</span><span>WED</span><span>THU</span><span>FRI</span><span>SAT</span><span>SUN</span></div>
    <div class="cal-grid">
      <span class="a">30</span><span class="b">1</span><span class="a">2</span><span class="a">3</span><span class="b">4</span><span class="b">5</span><span class="a">6</span>
      <span class="b">7</span><span class="a">8</span><span class="b">9</span><span class="a">10</span><span class="b">11</span><span class="b">12</span><span class="a">13</span>
      <span class="a">14</span><span class="b">15</span><span class="b">16</span><span class="a">17</span><span class="b">18</span><span class="a">19</span><span class="b">20</span>
      <span class="b">21</span><span class="a">22</span><span class="b">23</span><span class="a">24</span><span class="a">25</span><span class="b">26</span><span class="a">27</span>
      <span class="b">28</span><span class="b">29</span><span class="a">30</span><span class="b">31</span><span class="o">1</span><span class="o">2</span><span class="a">3</span>
    </div>
  </div>
  <div class="legend abs"><span><i style="background:var(--red)"></i>Booked</span><span><i style="background:var(--green)"></i>Available</span></div>
  <h2 class="price-title abs">Price and Availability</h2>
  <div class="price-text abs">
    <p>Sed ut perspiciatis unde omnis iste natus error sit voluptatem accusantium doloremque laudantium, totam rem aperiam, eaque ipsa quae ab illo inventore veritatis et quasi architecto beatae vitae dicta sunt explicabo. Nemo enim ipsam voluptatem quia voluptas sit aspernatur aut odit aut fugit,</p>
    <p>Ut enim ad minima veniam, quis nostrum exercitationem ullam corporis suscipit laboriosam, nisi ut aliquid ex ea commodi consequatur aliquam commodi consequatur...</p>
  </div>
  <div class="btn price-btn abs">&#9998; BOOK NOW</div>
</section>

<section class="gallery abs" role="img" aria-label="Misty green island hills behind the gallery">
  <h2 class="gallery-title abs">Gallery</h2>
  <svg class="gal-arrow abs" style="left:22px" width="22" height="60" viewBox="0 0 22 60"><path d="M20 2 2 30l18 28" fill="none" stroke="#fff" stroke-width="2"/></svg>
  <svg class="gal-arrow abs" style="left:1156px" width="22" height="60" viewBox="0 0 22 60"><path d="M2 2l18 28L2 58" fill="none" stroke="#fff" stroke-width="2"/></svg>
  <div class="gal-tile abs" style="left:102px;background:linear-gradient(180deg,#c9d0b0,#8d8a6a)" role="img" aria-label="Tall grass on the shore">
    <div class="gal-card abs"><h3>Quis autem veleum</h3><p>&#9998; Comments &nbsp;|&nbsp; &#9825; 3</p></div>
  </div>
  <div class="gal-tile abs" style="left:354px;background:linear-gradient(180deg,#2a3a2a,#5e6d5c 50%,#1c2620)" role="img" aria-label="Waterfall in a rainforest gorge"></div>
  <div class="gal-tile abs" style="left:604px;background:linear-gradient(180deg,#5aa0d8,#2e6fa6 50%,#1f5f86)" role="img" aria-label="Guests on the deck with a life ring and flag"></div>
  <div class="gal-tile abs" style="left:857px;background:linear-gradient(180deg,#7fb3d9,#5e8a6a 45%,#2e6f9a 70%,#1e5878)" role="img" aria-label="Island resort above a blue bay"></div>
</section>

<section class="contact">
  <h2 class="contact-title abs">Contact Form</h2>
  <div class="field abs" style="left:253px;top:1850px"><label>Enter Name</label><div class="box"></div></div>
  <div class="field abs" style="left:613px;top:1850px"><label>Enter Email</label><div class="box"></div></div>
  <div class="field abs" style="left:253px;top:1951px"><label>Phone</label><div class="box"></div></div>
  <div class="field abs" style="left:613px;top:1951px"><label>Address</label><div class="box"></div></div>
  <div class="field abs" style="left:253px;top:2048px"><label>Message</label><div class="box wide"></div></div>
  <div class="send-btn abs">SEND MESSAGE</div>
</section>

<section class="testimonials abs">
  <h2 class="testi-title abs">Testimonials &amp; Reviews</h2>
  <div class="t-arrow abs" style="left:30px"><svg width="10" height="14"><path d="M8 1 2 7l6 6" fill="none" stroke="#fff" stroke-width="2"/></svg></div>
  <div class="t-arrow abs" style="left:1136px"><svg width="10" height="14"><path d="M2 1l6 6-6 6" fill="none" stroke="#fff" stroke-width="2"/></svg></div>

  <div class="review abs" style="left:100px">
    <div class="avatar" style="background:#3b3b3b" role="img" aria-label="Reviewer portrait"></div>
    <div><q>“ Calm water, a warm crew and the best sunsets we have ever seen. Already planning our next trip.</q>
      <p class="name">ROSA LINDQVIST</p><p class="role">Retail Project Lead</p>
      <div class="stars"><span style="color:var(--star)">★★★★</span><span style="color:#fbd7c5">☆</span></div></div>
  </div>
  <div class="review abs" style="left:450px">
    <div class="avatar" style="background:#d9d4cc" role="img" aria-label="Reviewer portrait"></div>
    <div><q>“ Easy booking, quiet anchorages and snorkelling straight off the back step every single day.</q>
      <p class="name">MARCUS OHLEN</p><p class="role">Field Geologist from the Coast</p>
      <div class="stars"><span style="color:var(--star)">★★★★½</span></div></div>
  </div>
  <div class="review abs" style="left:800px">
    <div class="avatar" style="background:#e2d5c8" role="img" aria-label="Reviewer portrait"></div>
    <div><q>“ A relaxed week on the islands with a boat that felt like home. We loved every slow hour.</q>
      <p class="name">ANA WHITFIELD</p><p class="role">Primary School Teacher and Painter</p>
      <div class="stars"><span style="color:var(--star)">★★★★</span><span style="color:#fbd7c5">☆</span></div></div>
  </div>
</section>

<section class="store">
  <h2 class="h2 abs" style="left:96px;top:2910px">Bookings</h2>
  <p class="book-text abs">Ut enim ad minima veniam, quis nostrum exercitationem ullam corporis suscipit laboriosam, nisi ut aliquid ex ea commodi consequatur aliquam commodi consequatur...</p>
  <div class="book-photo abs" role="img" aria-label="Blue inflatable tender on the water"></div>
  <div class="btn book-btn abs">&#9998; BOOK NOW</div>
  <div class="divider abs"></div>

  <h2 class="h2 abs" style="left:596px;top:2910px">Our Store</h2>
  <div class="product abs" style="left:598px">
    <div class="img"><div style="width:120px;height:130px;background:#707070;border-radius:8px" role="img" aria-label="Grey t-shirt with boat print"></div></div>
    <h4>Quai architentcto</h4><p class="price">$78.09</p><span class="shop">SHOP NOW</span>
  </div>
  <div class="product abs" style="left:866px">
    <div class="img"><div style="width:130px;height:80px;background:#2242c8;border-radius:60px 60px 10px 10px" role="img" aria-label="Blue cap with boat print"></div></div>
    <h4>Magni doloren eaolupts</h4><p class="price">$78.09</p><span class="shop">SHOP NOW</span>
  </div>
  <div class="s-arrow abs" style="left:811px"><svg width="8" height="12"><path d="M7 1 2 6l5 5" fill="none" stroke="#555" stroke-width="1.5"/></svg></div>
  <div class="s-arrow abs" style="left:851px"><svg width="8" height="12"><path d="M1 1l5 5-5 5" fill="none" stroke="#555" stroke-width="1.5"/></svg></div>
</section>

<section class="extras abs">
  <svg class="abs" style="left:0;top:0" width="1200" height="406" viewBox="0 0 1200 406" role="img" aria-label="Guests relaxing on a catamaran deck at dusk">
    <defs>
      <linearGradient id="deck" x1="0" y1="0" x2="0" y2="1"><stop offset="0" stop-color="#4a4e55"/><stop offset=".5" stop-color="#2b2d31"/><stop offset="1" stop-color="#17181a"/></linearGradient>
    </defs>
    <rect width="1200" height="406" fill="url(#deck)"/>
    <polygon points="690,0 1200,0 1200,406 510,406" fill="#e8693a" fill-opacity=".82"/>
  </svg>
  <a class="abs" style="left:188px">WHAT TO BRING</a>
  <div class="extras-mark abs"></div>
  <a class="abs" style="left:744px">WHAT TO EXPECT</a>
</section>

<footer>
  <div class="brand footer-brand abs"><span>Quiet Tern</span><span class="brand-dot"></span></div>
  <div class="socials abs">
    <span style="background:var(--navy)"></span><span style="background:var(--navy)"></span><span style="background:var(--orange)"></span><span style="background:var(--orange)"></span><span style="background:var(--orange)"></span><span style="background:var(--navy)"></span>
  </div>
  <div class="vline abs"></div>
  <h3 class="foot-h abs" style="left:465px;top:3960px">Quick Links</h3>
  <ul class="links abs"><li>Home</li><li>Price and Availability</li><li>Gallery</li><li>Contact</li><li>Testimonials &amp; Reviews</li><li>Bookings &amp; Store</li><li>Misc</li></ul>
  <h3 class="foot-h abs" style="left:726px;top:3960px">Sign Up Newsletter</h3>
  <p class="news-text abs">Et harum quidem rerum facilis est expedita distinctio</p>
  <div class="news-input abs">Enter Email...</div>
  <div class="btn subscribe abs">SUBSCRIBE</div>
  <div class="foot-line abs"></div>
  <p class="copy abs">© Copyright 2018 Quiet Tern All Rights Reserved &nbsp;|&nbsp; Privacy policy</p>
</footer>

</body>
</html>
```